Guarding One's Body Using Sharp Steel Cover

Hi we are producing a self defense course entitled Guarding One's Body Using Sharp Steel: A Complete Manual For Learning The Finest And Handiest Wilderness Tool In Recorded History.

I listed this as a book cover but it will actually be a DVD set, but the book cover model works fine.

See below for design examples - I am thinking we need a cover that will appeal to military/survival type people.

Target Market(s)

survivalists, cops, preppers, gun owners, martial artists, and average people wanting to learn how to defend themselves

Industry/Entity Type

Defense

Requirements
Must have
• Title: GUARDING ONE'S BODY USING SHARP STEEL: A COMPLETE MANUAL FOR LEARNING THE FINEST AND HANDIEST WILDERNESS TOOL IN RECORDED HISTORY
Nice to have
• Please look at these sample designs from other books as a model:
• https://files.plorvexa.org/media/en/4/27/BrindelQXMP.jpg - This stye is ideal.
• Other good examples:
• https://pics2.talvorn.com/8143907_k370.jpg
• http://m.zephquill.com/titles/2719058463k/48071935.jpg
• http://img.crondelmart.com/pics/P/73Tm58QyzFr._BX_KL410_TR316,410_.jpg
• http://3.cdn.wendoplix.net/-RTyZWLMMKAQ/BNWq_hufxaT/BBBBBBBBv8G/DKNp815ZaXW/s1600/Q4710392.JPG

```html
<!DOCTYPE html>
<html lang="en">
<head>
<meta charset="utf-8">
<title>Guarding One's Body Using Sharp Steel — Cover</title>
<link rel="stylesheet" href="https://fonts.googleapis.com/css2?family=Teko:wght@600;700&family=Oswald:wght@500;600;700&display=swap">
<style>
  :root {
    --stage: #ececec;
    --wood-light: #c49a72;
    --wood-mid: #b88a62;
    --wood-dark: #a77853;
    --title-green: #1e4a1c;
    --ink: #121212;
  }
  * { margin: 0; padding: 0; box-sizing: border-box; }
  html, body { width: 1200px; height: 1000px; overflow: hidden; }
  body {
    background: var(--stage);
    display: flex;
    align-items: center;
    justify-content: center;
  }
  .cover {
    position: relative;
    width: 560px;
    height: 860px;
    overflow: hidden;
  }
  .cover-wood {
    position: absolute;
    inset: 0;
    background:
      linear-gradient(160deg, transparent 0 24%, rgba(255,235,210,0.12) 24% 40%, transparent 40%),
      linear-gradient(180deg, var(--wood-light), var(--wood-mid) 55%, var(--wood-dark));
  }
  .cover-content {
    position: relative;
    height: 100%;
    padding: 40px 30px 40px;
    display: flex;
    flex-direction: column;
    align-items: center;
  }
  .title {
    font-family: "Teko", sans-serif;
    font-weight: 700;
    color: var(--title-green);
    text-transform: uppercase;
    text-align: center;
    line-height: 0.9;
    white-space: nowrap;
  }
  .title-line { display: block; font-size: 64px; letter-spacing: 0.5px; }
  .title-keyword {
    display: block;
    margin-top: 14px;
    font-size: 200px;
    line-height: 0.78;
    letter-spacing: 2px;
  }
  .subtitle {
    margin-top: 56px;
    font-family: "Oswald", sans-serif;
    font-weight: 600;
    color: var(--ink);
    text-align: center;
    line-height: 1.22;
    white-space: nowrap;
  }
  .subtitle span { display: block; }
  .subtitle .s1 { font-size: 27px; }
  .subtitle .s2 { font-size: 24px; }
  .subtitle .s3 { font-size: 24px; }
  .subtitle .s4 { font-size: 28px; }
  .subtitle .s5 { font-size: 36px; }
  .author {
    margin-top: auto;
    font-family: "Oswald", sans-serif;
    font-weight: 700;
    font-size: 50px;
    color: var(--ink);
    text-transform: uppercase;
    letter-spacing: 0.5px;
    white-space: nowrap;
  }
</style>
</head>
<body>
  <article class="cover">
    <div class="cover-wood" role="img" aria-label="Scratched light wooden cutting board texture"></div>
    <div class="cover-content">
      <h1 class="title">
        <span class="title-line">Guarding One's</span>
        <span class="title-line">Body Using Sharp</span>
        <span class="title-keyword">Steel</span>
      </h1>
      <p class="subtitle">
        <span class="s1">A Complete Manual</span>
        <span class="s2">For Learning The Finest</span>
        <span class="s3">And Handiest Wilderness</span>
        <span class="s4">Tool In Recorded</span>
        <span class="s5">History</span>
      </p>
      <p class="author">Dale R. Whitcombe</p>
    </div>
  </article>
</body>
</html>
```